5 Planner Covers for Teacher Planners

Hello,
I currently run a Speech-Language Pathologist website and have created a planner for my fellow Speech Therapist. I would like someone to create 5 different planner covers so my followers will have different options to choose from.
Here is my planner from last year to give you an idea of what the planner will look like http://www.talkwellnook.example/free-slp-planner/
My followers are mostly women aged 25-50. However, I don't want the covers to be overly girly or excessive with flowers. Simple is better.
I'd also like there to be an editable text box to allow the Speech Therapist to type their name on their cover if they wish.
Planner Cover can say any of the following: SLP Planner, Planner, Speech Therapy Planner, Speech-Language Pathologist (maybe this title could be editable as well??).
To give you an idea I have uploaded a screenshot of last year's planners cover that I made myself.
What I am looking for:
-Size 8.5" by 11"
-5 different planner covers
-1 gender-neutral cover
-simple design
-limited flowers (or overly girly
-text box to add a personal name
-Possible titles: SLP Planner, Planner, Speech Therapy Planner, Speech-Language Pathologist (maybe this title could be editable as well??)
Target Market(s)
Women aged 25-50
Colors
Designer to choose colors to be used in the design.
Requirements
Must have
- What I am looking for:
-Size 8.5" by 11"
-1 gender-neutral cover
-simple design
Nice to have
- I've uploaded some that I like from Craftly to give you an idea.
Here is my craftly store https://www.craftly.example/shop/QuietMeadowHome to give you an idea of things I like.
I like Marla Hensley and her simple elegant rustic style.

```html
<!DOCTYPE html>
<html lang="en">
<head>
<meta charset="utf-8">
<title>SLP Planner Cover</title>
<link rel="stylesheet" href="https://fonts.googleapis.com/css2?family=Josefin+Sans:wght@300;400&display=swap">
<style>
  :root {
    --cover-lilac: #cba0cb;
    --title-violet: #662d91;
    --ghost-lilac: #d5b1d5;
    --ornament-lilac: #dcbfdc;
    --flower-pink: #e6c6e3;
    --flower-rose: #c98dc4;
    --label-white: #ffffff;
    --label-rule: #b57fb8;
  }
  html, body {
    margin: 0;
    padding: 0;
    overflow: hidden;
    background: var(--cover-lilac);
  }
  .cover {
    position: relative;
    width: 927px;
    height: 1200px;
    overflow: hidden;
    background: var(--cover-lilac);
    font-family: "Josefin Sans", sans-serif;
  }
  .cover__art {
    position: absolute;
    inset: 0;
    width: 927px;
    height: 1200px;
  }
  .ornament-band {
    position: absolute;
    left: 7px;
    top: 11px;
    width: 913px;
    height: 171px;
    border-radius: 60px;
    background: linear-gradient(180deg, var(--ornament-lilac), var(--cover-lilac));
    opacity: 0.7;
  }
  .flower-spray {
    position: absolute;
    left: 0;
    top: 825px;
    width: 469px;
    height: 350px;
    border-radius: 0 60% 40% 0;
    background: radial-gradient(ellipse at 40% 55%, var(--flower-pink) 0%, var(--flower-rose) 55%, var(--cover-lilac) 80%);
  }
  .ghost-text { fill: var(--ghost-lilac); font-weight: 300; }
  .title-text { fill: var(--title-violet); font-weight: 400; }
</style>
</head>
<body>
<main class="cover">
  <div class="ornament-band" role="img" aria-label="Row of light lilac swirl ornaments"></div>

  <svg class="cover__art" viewBox="0 0 927 1200" xmlns="http://www.w3.org/2000/svg">
    <text class="ghost-text" x="44" y="553" font-size="495" textLength="615" lengthAdjust="spacingAndGlyphs">SLP</text>
    <text class="ghost-text" transform="translate(883 934) rotate(-90)" font-size="258" textLength="716" lengthAdjust="spacingAndGlyphs">PLANNER</text>

    <text class="title-text" x="200" y="585" font-size="200" textLength="252" lengthAdjust="spacingAndGlyphs">SLP</text>
    <text class="title-text" x="205" y="727" textLength="418" lengthAdjust="spacingAndGlyphs"><tspan font-size="150">P</tspan><tspan font-size="112">LANNER</tspan></text>

    <g class="name-label">
      <rect x="487" y="960" width="418" height="196" rx="60" fill="var(--label-white)" stroke="var(--label-white)" stroke-width="2"/>
      <rect x="492" y="965" width="408" height="186" rx="56" fill="var(--label-white)" stroke="var(--label-rule)" stroke-width="1.5"/>
      <line x1="534" y1="1016" x2="865" y2="1016" stroke="var(--label-rule)" stroke-width="1.5"/>
      <line x1="534" y1="1068" x2="865" y2="1068" stroke="var(--label-rule)" stroke-width="1.5"/>
      <line x1="534" y1="1116" x2="865" y2="1116" stroke="var(--label-rule)" stroke-width="1.5"/>
    </g>
  </svg>

  <div class="flower-spray" role="img" aria-label="Spray of pale pink blossoms with falling petals"></div>
</main>
</body>
</html>
```